Graphic Design Project

We are currently undertaking a new business venture. We have developed a business strategy which we wish to present to our prospective business partner as a one page visual.
The business strategy which we developed is in word format. We would like to be able to present our partner with a chart that is more professional visually.
Ideally we would like to be able to edit the document, so that as the strategy changes we can update it - but this is not essential if it hinders the design. Please let us know what format you will be providing the document in.
I have attached a copy of the chart that we created. When we pick the successful design we will send you our company name and logo be included in the design.
Target Market(s)
We are a training company and our new business venture is with another training and development company
Industry/Entity Type
Business
Requirements
Nice to have
- Editable version

```html
<!DOCTYPE html>
<html lang="en">
<head>
<meta charset="utf-8">
<title>Business Strategy Overview</title>
<link href="https://fonts.googleapis.com/css2?family=Tinos:wght@400;700&display=swap" rel="stylesheet">
<style>
  :root{
    --band-dark:#1b1a52;
    --band-light:#6d95cc;
    --green-top:#1c9c7a;
    --green-bottom:#0d6a52;
    --purple-top:#9a6aa6;
    --purple-bottom:#6c3d7c;
    --red-top:#ee2a2f;
    --red-bottom:#c3121b;
    --divider:#f2c51c;
    --ink:#ffffff;
    --paper:#ffffff;
  }
  html,body{margin:0;padding:0;overflow:hidden;background:var(--paper);}
  .canvas{position:relative;width:1200px;height:849px;overflow:hidden;background:var(--paper);
    font-family:"Tinos","Times New Roman",serif;color:var(--ink);}
  .band{position:absolute;left:0;width:1200px;height:36px;
    background:linear-gradient(90deg,var(--band-dark) 0%,#2f3f86 35%,var(--band-light) 62%,#34488e 80%,var(--band-dark) 100%);}
  .band--top{top:0;}
  .band--bottom{bottom:0;height:39px;}
  .shapes{position:absolute;left:0;top:0;}
  .block{position:absolute;box-sizing:border-box;}
  .center{text-align:center;}
  .title{font-weight:700;font-size:22px;line-height:1.2;margin:0;}
  .small{font-size:12px;line-height:1.35;margin:0;}
  .small + .small{margin-top:12px;}
  .stage-title{font-weight:700;font-size:22px;text-align:center;margin:0 0 8px;}
  .bullets{list-style:none;margin:0;padding:0 0 0 22px;font-size:15px;line-height:1.32;}
  .bullets li::before{content:"» ";}
  .bullets--tight{font-size:13.5px;line-height:1.22;}
  .red-title{font-weight:700;font-size:22px;text-align:center;margin:0;}
  .red-list{list-style:none;margin:0;padding:0;font-size:11.5px;line-height:1.3;}
  .red-list li{margin-bottom:12px;}
  .sub-title{font-weight:700;font-size:13.5px;margin:0;}
  .body-text{font-size:13.5px;line-height:1.3;margin:0;}
</style>
</head>
<body>
<div class="canvas">
  <div class="band band--top"></div>
  <div class="band band--bottom"></div>

  <svg class="shapes" width="1200" height="849" viewBox="0 0 1200 849">
    <defs>
      <linearGradient id="goal-fill" x1="0" y1="0" x2="0" y2="1">
        <stop offset="0" stop-color="var(--green-top)"/>
        <stop offset="1" stop-color="var(--green-bottom)"/>
      </linearGradient>
      <linearGradient id="stage-fill" x1="0" y1="0" x2="0" y2="1">
        <stop offset="0" stop-color="var(--purple-top)"/>
        <stop offset="1" stop-color="var(--purple-bottom)"/>
      </linearGradient>
      <linearGradient id="detail-fill" x1="0" y1="0" x2="0" y2="1">
        <stop offset="0" stop-color="var(--red-top)"/>
        <stop offset="1" stop-color="var(--red-bottom)"/>
      </linearGradient>
    </defs>

    <!-- goal boxes -->
    <g fill="url(#goal-fill)">
      <path d="M82 60H274V258H196L178 282L160 258H82Z"/>
      <path d="M298 60H490V258H412L394 282L376 258H298Z"/>
      <path d="M514 60H706V258H628L610 282L592 258H514Z"/>
      <path d="M730 60H922V258H844L826 282L808 258H730Z"/>
      <path d="M936 60H1128V258H1050L1032 282L1014 258H936Z"/>
    </g>

    <!-- stage chevrons -->
    <g fill="url(#stage-fill)">
      <path d="M60 274H262L276 360L262 447H74Q60 447 60 433Z"/>
      <path d="M280 274H478L492 360L478 447H280L294 360Z"/>
      <path d="M496 274H694L708 360L694 447H496L510 360Z"/>
      <path d="M712 274H910L924 360L910 447H712L726 360Z"/>
      <path d="M928 274H1130Q1144 274 1144 288V433Q1144 447 1130 447H928L942 360Z"/>
    </g>

    <!-- detail boxes -->
    <g fill="url(#detail-fill)">
      <path d="M93 446H146L176 405L206 446H270V735H93Z"/>
      <path d="M307 446H363L393 405L423 446H475V783H307Z"/>
      <path d="M523 446H691V675H523Z"/>
      <path d="M800 446H838L868 405L898 446H1008V657H800Z"/>
    </g>

    <!-- dividers -->
    <g stroke="var(--divider)" stroke-width="3" fill="none">
      <line x1="307" y1="627" x2="475" y2="627"/>
      <line x1="307" y1="694" x2="475" y2="694"/>
      <polyline points="800,555 860,555 872,545 884,560 896,552 1008,552"/>
    </g>
  </svg>

  <!-- goal text -->
  <div class="block center" style="left:90px;top:66px;width:176px;">
    <p class="title">GR- Strategy/<br>tactics</p>
    <p class="small" style="margin-top:22px;">OC- Assist to with<br>developing operations<br>and expansion</p>
  </div>
  <div class="block center" style="left:306px;top:74px;width:176px;">
    <p class="title">GR</p>
    <p class="small" style="margin-top:24px;">Develop a new team.<br>Need strong sales<br>people in, and cold callers.<br>Import new capacity</p>
  </div>
  <div class="block" style="left:522px;top:74px;width:180px;">
    <p class="title center">GR</p>
    <p class="small" style="margin-top:22px;">Lean on current and further<br>develop.</p>
    <p class="small">OC- Technology development:<br>SlatePad delivery with dashboard</p>
    <p class="small">OC- Leverage scope</p>
  </div>
  <div class="block" style="left:738px;top:74px;width:180px;">
    <p class="title center">GR</p>
    <p class="small" style="margin-top:22px;">Build on current.</p>
    <p class="small">OC- develop metrics/<br>dashboard</p>
    <p class="small">External: import capacity</p>
  </div>
  <div class="block center" style="left:944px;top:148px;width:176px;">
    <p class="small">Demonstrate and leverage<br>the outcome.</p>
  </div>

  <!-- stage text -->
  <div class="block" style="left:70px;top:284px;width:196px;">
    <p class="stage-title">Contact</p>
    <ul class="bullets" style="padding-left:42px;"><li>Referrals</li><li>Marketing</li><li>Strong Website</li></ul>
  </div>
  <div class="block" style="left:294px;top:284px;width:186px;">
    <p class="stage-title">Sales</p>
    <ul class="bullets" style="padding-left:30px;"><li>Listening</li><li>Explanation</li><li>Value Prop</li></ul>
  </div>
  <div class="block" style="left:506px;top:284px;width:196px;">
    <p class="stage-title" style="margin-bottom:2px;">Solution</p>
    <ul class="bullets bullets--tight" style="padding-left:16px;"><li>Diagnostic</li><li>Funded VET</li><li>Custom</li><li>EI/ Behaviour</li><li>Consulting: Partner/<br>&nbsp;&nbsp;&nbsp;Internal</li></ul>
  </div>
  <div class="block" style="left:724px;top:284px;width:196px;">
    <p class="stage-title" style="margin-bottom:4px;">Measurement</p>
    <ul class="bullets bullets--tight" style="padding-left:12px;"><li>Metric Dashboard</li><li>Measure Changes</li><li>Based on Intervention?</li><li>Effect of intervention<br>&nbsp;&nbsp;&nbsp;on Performance</li></ul>
  </div>
  <div class="block" style="left:940px;top:284px;width:196px;">
    <p class="stage-title">ROI</p>
    <ul class="bullets" style="padding-left:18px;"><li>Increased financial<br>&nbsp;&nbsp;&nbsp;performance</li><li>Case Studies</li></ul>
  </div>

  <!-- detail text -->
  <div class="block" style="left:100px;top:454px;width:164px;">
    <p class="red-title" style="margin-bottom:18px;">Channels</p>
    <ul class="red-list">
      <li>Current- maximise</li>
      <li>Website-improve<br>and increase SEO</li>
      <li>Networks – OC<br>introduce new clients</li>
      <li>Partnership</li>
      <li>Existing Clients</li>
      <li>Private equity – solution sell</li>
      <li>Referrals</li>
    </ul>
  </div>
  <div class="block" style="left:316px;top:452px;width:156px;">
    <p class="red-title" style="font-size:21px;margin-bottom:8px;">Market Split</p>
    <ul class="red-list" style="font-size:11px;">
      <li>Targeting Change:<br>compelling change model</li>
      <li>Projects –Performance Link</li>
      <li>Scale – Genuine mandate for<br>change/growth</li>
      <li>Generating warm leads</li>
    </ul>
  </div>
  <div class="block center" style="left:307px;top:636px;width:168px;">
    <p class="sub-title">Develop Raving Fans</p>
    <p class="small" style="font-size:11px;margin-top:12px;">Experiential Education Sale</p>
  </div>
  <div class="block" style="left:316px;top:700px;width:156px;">
    <p class="sub-title center" style="font-size:16px;">Work on Model</p>
    <p class="small" style="font-size:11px;">Small team – heavily<br>incentivised</p>
    <p class="small" style="font-size:11px;margin-top:14px;">Solution Sell/Focus</p>
  </div>
  <div class="block" style="left:532px;top:460px;width:156px;">
    <p class="body-text">Broaden what we deliver</p>
    <p class="body-text" style="margin-top:18px;">i.e. More intensive<br>intervention. Delivery,<br>Behaviour change<br>coaching</p>
  </div>
  <div class="block" style="left:818px;top:460px;width:186px;">
    <p class="body-text">Making the point that training<br>is an investment with a<br>quantifiable outcome.<br>ROI of training very powerful</p>
  </div>
  <div class="block" style="left:818px;top:570px;width:186px;">
    <p class="sub-title" style="font-size:15px;">Efficiency Gains</p>
    <p class="small">Sales force</p>
    <p class="small" style="margin-top:18px;">Centralise Functions</p>
  </div>
</div>
</body>
</html>
```